Welcome Card

We are a property management company and I need to attach this postcard to 2 packages of microwave popcorn as a welcome gift to our new tenant.Here is the copy for the postcard (FRONT SIDE): Just "popped" in to make sure your apartment was ready for you! Enjoy your Stay.........UNITED APARTMENTSBACK SIDE: Welcome image with the words "Thank You"

Industry/Entity Type

It Company

Font styles to use
Sans Serif

```html
<!DOCTYPE html>
<html lang="en">
<head>
<meta charset="utf-8">
<title>Bramble Apartments Welcome Card</title>
<link rel="stylesheet" href="https://fonts.googleapis.com/css2?family=Fraunces:opsz,wght@9..144,700;9..144,900&family=Questrial&display=swap">
<style>
  :root {
    --bg: #262626;
    --card: #ffffff;
    --card-shade: #ececec;
    --brand-blue: #1b5aa8;
    --ink: #1c1c1c;
    --kernel-light: #fbf6d8;
    --kernel-dark: #e2d49a;
  }
  * { box-sizing: border-box; margin: 0; padding: 0; }
  html, body { width: 1200px; height: 1200px; overflow: hidden; }
  body { background: var(--bg); position: relative; font-family: "Questrial", sans-serif; }

  .card {
    position: absolute;
    background: var(--card);
    box-shadow: 0 2px 6px rgba(0,0,0,.5);
    overflow: hidden;
  }

  /* Back side */
  .card-back {
    left: 448px; top: 36px; width: 718px; height: 552px;
    background: linear-gradient(180deg, var(--card) 60%, #f6f6f6 100%);
    text-align: center;
  }
  .card-back .welcome {
    position: absolute; left: 0; right: 0; top: 226px;
    font-family: "Fraunces", serif; font-weight: 900;
    font-size: 76px; line-height: 1; color: var(--brand-blue);
    letter-spacing: -1px;
  }
  .card-back .thanks {
    position: absolute; left: 0; right: 0; top: 378px;
    font-size: 27px; color: var(--ink);
  }

  /* Front side */
  .card-front {
    left: 52px; top: 612px; width: 720px; height: 554px;
    background: radial-gradient(ellipse at 60% 10%, var(--card) 45%, var(--card-shade) 100%);
  }
  .headline-kicker {
    position: absolute; left: 48px; top: 116px;
    font-family: "Fraunces", serif; font-weight: 900;
    font-size: 30px; line-height: 1; color: var(--ink); letter-spacing: 1px;
  }
  .headline-main {
    position: absolute; left: 44px; top: 141px;
    font-family: "Fraunces", serif; font-weight: 900;
    font-size: 96px; line-height: 1; color: var(--brand-blue);
    letter-spacing: -2px; white-space: nowrap;
  }
  .popcorn {
    display: inline-block; width: 72px; height: 78px;
    vertical-align: -6px; margin: 0 -2px;
    border-radius: 46% 52% 40% 48%;
    background: radial-gradient(circle at 40% 35%, var(--kernel-light) 40%, var(--kernel-dark) 100%);
  }
  .tagline {
    position: absolute; left: 48px; top: 262px;
    font-size: 18px; line-height: 24px; color: var(--ink);
  }
  .stay-band {
    position: absolute; left: 0; top: 440px; width: 454px; height: 88px;
    background: var(--brand-blue);
    display: flex; align-items: center; padding-left: 44px;
    font-family: "Fraunces", serif; font-weight: 700;
    font-size: 27px; color: #fff; letter-spacing: 1px; white-space: nowrap;
  }
  .band-end {
    position: absolute; left: 688px; top: 440px; width: 32px; height: 88px;
    background: var(--brand-blue);
  }
  .brand {
    position: absolute; left: 474px; top: 440px; width: 196px; height: 88px;
    display: flex; align-items: center; justify-content: center; gap: 8px;
    font-size: 22px; line-height: 1.1; color: var(--brand-blue); text-align: center;
  }
  .brand-mark { width: 14px; height: 14px; background: var(--brand-blue); flex: none; }
</style>
</head>
<body>
  <section class="card card-back" aria-label="Card back">
    <h1 class="welcome">Welcome</h1>
    <p class="thanks">Thank You</p>
  </section>

  <section class="card card-front" aria-label="Card front">
    <p class="headline-kicker">JUST</p>
    <p class="headline-main">p<span class="popcorn" role="img" aria-label="Popped kernel of popcorn standing in for the letter o"></span>pped</p>
    <p class="tagline">in to make sure<br>your apartment was ready for you!</p>
    <div class="stay-band">ENJOY YOUR STAY .......</div>
    <div class="brand"><span class="brand-mark"></span><span>BRAMBLE<br>APARTMENTS</span></div>
    <div class="band-end"></div>
  </section>
</body>
</html>
```